Electrical contractor Brochure design

We are looking a elegant brochure design for our new branding campaign. Logo ai file is attached. We mainly work in power plants and manufacturing facilities. We would like some pictures to show those types of facilities.

Target Market(s)

Industrial commercial electrician

Industry/Entity Type

Contractor

Font styles to use
Sans Serif

```html
<!DOCTYPE html>
<html lang="en">
<head>
<meta charset="utf-8">
<title>Voltline Electric – Brochure Cover</title>
<link rel="stylesheet" href="https://fonts.googleapis.com/css2?family=Michroma&family=Open+Sans:ital,wght@0,400;0,700;0,800;1,800&display=swap">
<style>
  :root {
    --backdrop: #9a9a9a;
    --paper: #ffffff;
    --curve-grey: #e6e6ec;
    --night-top: #1f2a78;
    --night-mid: #33407f;
    --night-low: #6b6e86;
    --brand-red: #b5112a;
    --band-black: #111111;
    --ink-dark: #1a1a1a;
    --text-light: #ffffff;
  }
  * { box-sizing: border-box; margin: 0; padding: 0; }
  html, body {
    width: 1200px;
    height: 788px;
    overflow: hidden;
    background: var(--backdrop);
  }
  .cover {
    position: absolute;
    left: 345px;
    top: 34px;
    width: 510px;
    height: 720px;
    background: var(--paper);
    overflow: hidden;
  }
  .cover-shapes {
    position: absolute;
    inset: 0;
    width: 510px;
    height: 720px;
  }
  .web-address {
    position: absolute;
    left: 498px;
    top: 22px;
    transform-origin: 0 0;
    transform: rotate(90deg);
    font-family: "Open Sans", sans-serif;
    font-weight: 700;
    font-size: 15px;
    letter-spacing: 0.3px;
    color: var(--ink-dark);
    white-space: nowrap;
  }
  .web-address .domain { color: var(--brand-red); }
  .headline {
    position: absolute;
    left: 150px;
    top: 330px;
    font-family: "Michroma", sans-serif;
    font-size: 25px;
    line-height: 30px;
    color: var(--text-light);
    letter-spacing: 0.5px;
  }
  .subhead {
    position: absolute;
    left: 150px;
    top: 394px;
    font-family: "Open Sans", sans-serif;
    font-style: italic;
    font-weight: 800;
    font-size: 16px;
    color: var(--text-light);
    letter-spacing: 0.4px;
  }
  .subhead-rule {
    position: absolute;
    left: 150px;
    top: 420px;
    width: 240px;
    height: 3px;
    background: var(--text-light);
  }
  .intro {
    position: absolute;
    left: 150px;
    top: 432px;
    width: 320px;
    font-family: "Open Sans", sans-serif;
    font-size: 11.5px;
    line-height: 16px;
    color: var(--text-light);
  }
  .brand {
    position: absolute;
    left: 150px;
    top: 660px;
    height: 48px;
    display: flex;
    align-items: center;
    gap: 10px;
  }
  .brand-dot {
    width: 30px;
    height: 30px;
    border-radius: 50%;
    background: var(--brand-red);
  }
  .brand-name {
    font-family: "Open Sans", sans-serif;
    font-weight: 700;
    font-size: 22px;
    color: var(--text-light);
    letter-spacing: 0.5px;
  }
</style>
</head>
<body>
  <main class="cover">
    <svg class="cover-shapes" viewBox="0 0 510 720" xmlns="http://www.w3.org/2000/svg">
      <defs>
        <linearGradient id="night-sky" x1="0" y1="0" x2="0" y2="1">
          <stop offset="0" stop-color="var(--night-top)"/>
          <stop offset="0.55" stop-color="var(--night-mid)"/>
          <stop offset="1" stop-color="var(--night-low)"/>
        </linearGradient>
      </defs>
      <circle class="grey-arc" cx="40" cy="170" r="330" fill="var(--curve-grey)"/>
      <circle class="plant-photo" cx="40" cy="130" r="310" fill="url(#night-sky)"
              role="img" aria-label="Photograph of a power plant at night with lit smokestacks and steam"/>
      <circle class="red-disc" cx="350" cy="440" r="245" fill="var(--brand-red)" opacity="0.94"/>
      <rect class="brand-band" x="0" y="650" width="510" height="70" fill="var(--band-black)"/>
      <path class="band-curve" d="M0 650 Q60 690 160 720 L0 720 Z" fill="var(--paper)"/>
    </svg>

    <p class="web-address">www.<span class="domain">voltline-electric</span>.com</p>

    <h1 class="headline">LOREM IPSUM<br>DOLOR SIT AMET</h1>
    <p class="subhead">Consectetur Adipiscing Elit</p>
    <div class="subhead-rule"></div>
    <p class="intro">Lorem ipsum dolor sit amet, consectetur adipiscing elit. Vestibulum dignissim, ante in faucibus volutpat, nisl augue consequat sem, sit amet dapibus purus neque sed ipsum. Cras quis elementum leo. Maecenas gravida pellentesque lacus at consequat. Aliquam pellentesque malesuada fringilla.</p>

    <div class="brand">
      <span class="brand-dot"></span>
      <span class="brand-name">Voltline Electric</span>
    </div>
  </main>
</body>
</html>
```